WXO Business Card Design

Business card design per the attached files.

Target Market(s)

Government and military officials, aerospace companies and aviation professionals

Industry/Entity Type

Business

```html
<!DOCTYPE html>
<html lang="en">
<head>
<meta charset="utf-8">
<title>WXO Business Card</title>
<link href="https://fonts.googleapis.com/css2?family=Open+Sans:wght@400;600;700;800&display=swap" rel="stylesheet">
<style>
  :root {
    --bg: #e6e6e6;
    --card-white: #ffffff;
    --card-back: #f3f3f3;
    --brand-blue: #1b8ad6;
    --brand-navy: #1d3f8f;
    --ink: #1b1b1b;
    --ink-soft: #4a4a4a;
    --band-dark: #1c1c1c;
    --globe-grey: #9a9a9a;
  }
  * { margin: 0; padding: 0; box-sizing: border-box; }
  html, body { width: 1200px; height: 675px; overflow: hidden; }
  body {
    background: var(--bg);
    font-family: "Open Sans", Arial, sans-serif;
    position: relative;
  }
  .card {
    position: absolute;
    top: 188px;
    width: 520px;
    height: 298px;
    overflow: hidden;
    box-shadow: 0 6px 18px rgba(0,0,0,0.12);
  }
  .card-front { left: 60px; background: var(--card-white); }
  .card-back { left: 620px; background: var(--card-back); }

  .wordmark {
    display: flex;
    align-items: center;
    gap: 8px;
    color: var(--ink);
    font-weight: 800;
    line-height: 1;
  }
  .wordmark-dot {
    border-radius: 50%;
    background: var(--brand-blue);
    flex: none;
  }
  .wordmark-text { display: flex; flex-direction: column; }
  .wordmark-name { letter-spacing: 1px; }
  .wordmark-sub { letter-spacing: 0.5px; margin-top: 4px; }

  .card-front .wordmark { position: absolute; left: 120px; top: 64px; }
  .card-front .wordmark-dot { width: 14px; height: 14px; }
  .card-front .wordmark-name { font-size: 44px; }
  .card-front .wordmark-sub { font-size: 15px; }

  .tagline-band {
    position: absolute;
    left: 0; right: 0; top: 176px;
    height: 34px;
    background: var(--brand-blue);
    color: #fff;
    font-size: 16px;
    letter-spacing: 3px;
    text-align: center;
    line-height: 34px;
  }

  .card-back .wordmark { position: absolute; left: 40px; top: 42px; }
  .card-back .wordmark-dot { width: 9px; height: 9px; }
  .card-back .wordmark-name { font-size: 27px; }
  .card-back .wordmark-sub { font-size: 10px; }
  .division {
    position: absolute; left: 128px; top: 96px;
    font-size: 10px; font-weight: 700; color: var(--ink);
  }

  .person { position: absolute; left: 40px; top: 126px; }
  .person-name { font-size: 14px; font-weight: 700; color: var(--brand-blue); }
  .person-role { font-size: 8.5px; color: var(--ink-soft); letter-spacing: 0.5px; margin-top: 1px; }
  .person-mobile { font-size: 10.5px; font-weight: 700; color: var(--ink); margin-top: 2px; display: flex; align-items: center; gap: 5px; }

  .contact-list { position: absolute; left: 40px; top: 196px; list-style: none; font-size: 10.5px; color: var(--ink); }
  .contact-list li { display: flex; align-items: center; gap: 6px; margin-bottom: 3px; }
  .contact-list .phone-main { color: var(--brand-blue); font-weight: 600; }
  .contact-list .sep { margin-left: 8px; display: inline-flex; align-items: center; gap: 5px; }
  .icon { width: 10px; height: 10px; flex: none; }

  .globe-art {
    position: absolute; right: 6px; top: 10px;
    width: 250px; height: 210px;
    border-radius: 50%;
    background: radial-gradient(circle at 45% 45%, #d9d9d9 0%, var(--globe-grey) 60%, #cfd8ec 85%, rgba(29,63,143,0.35) 100%);
  }
  .bottom-band { position: absolute; left: 0; bottom: 0; width: 520px; height: 80px; }
</style>
</head>
<body>

<section class="card card-front">
  <div class="wordmark">
    <span class="wordmark-dot"></span>
    <div class="wordmark-text">
      <span class="wordmark-name">HALCYON</span>
      <span class="wordmark-sub">Training Group</span>
    </div>
  </div>
  <div class="tagline-band">LIVE • SYNTHETIC • NETWORKED</div>
</section>

<section class="card card-back">
  <div class="globe-art" role="img" aria-label="Illustration of a grey wire-frame globe circled by blue flight paths with aircraft"></div>

  <svg class="bottom-band" viewBox="0 0 520 80" aria-hidden="true">
    <path d="M300 14 Q310 4 325 4 L520 4 L520 80 L0 80 L0 26 L290 26 Q296 26 300 14 Z" fill="var(--brand-blue)"/>
    <path d="M310 22 Q318 12 332 12 L520 12 L520 80 L0 80 L0 34 L298 34 Q305 34 310 22 Z" fill="var(--band-dark)"/>
  </svg>

  <div class="wordmark">
    <span class="wordmark-dot"></span>
    <div class="wordmark-text">
      <span class="wordmark-name">HALCYON</span>
      <span class="wordmark-sub">Training Group</span>
    </div>
  </div>
  <div class="division">Nordfar Air Ehf</div>

  <div class="person">
    <div class="person-name">Einar T. Halldorsson</div>
    <div class="person-role">PRINCIPAL</div>
    <div class="person-mobile">
      <svg class="icon" viewBox="0 0 10 10" aria-hidden="true"><rect x="2.5" y="0.5" width="5" height="9" rx="1" fill="none" stroke="var(--brand-blue)" stroke-width="1"/></svg>
      +354 600 1834
    </div>
  </div>

  <ul class="contact-list">
    <li class="phone-main">
      <svg class="icon" viewBox="0 0 10 10" aria-hidden="true"><path d="M2 1 L4 1 L4.5 3 L3.3 3.8 Q4.3 5.8 6.2 6.7 L7 5.5 L9 6 L9 8 Q8.5 9 7.5 9 Q1 8 1 2.5 Q1 1.5 2 1 Z" fill="var(--brand-blue)"/></svg>
      +354 500 4726
    </li>
    <li>
      <svg class="icon" viewBox="0 0 10 10" aria-hidden="true"><rect x="0.5" y="2" width="9" height="6" fill="var(--ink)"/><path d="M0.5 2 L5 5.5 L9.5 2" fill="none" stroke="#fff" stroke-width="0.8"/></svg>
      einar@wxo.is
      <span class="sep">
        <svg class="icon" viewBox="0 0 10 10" aria-hidden="true"><circle cx="5" cy="5" r="4.3" fill="none" stroke="var(--ink)"/><ellipse cx="5" cy="5" rx="1.8" ry="4.3" fill="none" stroke="var(--ink)" stroke-width="0.8"/><line x1="0.7" y1="5" x2="9.3" y2="5" stroke="var(--ink)" stroke-width="0.8"/></svg>
        www.wxo.is
      </span>
    </li>
    <li>
      <svg class="icon" viewBox="0 0 10 10" aria-hidden="true"><path d="M5 9.5 Q1.5 5.5 1.5 3.8 A3.5 3.5 0 0 1 8.5 3.8 Q8.5 5.5 5 9.5 Z" fill="var(--ink)"/><circle cx="5" cy="3.8" r="1.3" fill="#fff"/></svg>
      Hlidarvegur 12 105 Reykjavik Iceland
    </li>
  </ul>
</section>

</body>
</html>
```